Business Card Design for an international medical business

We need a professional and elegant business card design with fashionable graphic element. Our company is located in Hong Kong with three worldwide production lines for medical equipment(surgical face masks, N95, face shields and so on). Our factories all contain medical standard ISOs and all product fulfill Marwick lab and KTR testing standards.

We would like to see designs that show the impression of our professional expertise, formal corporate image with creative thinking work style and inspiring global concept. We want the content in both English and Japanese on the same card. We also want to print our the patent trade mark and company logo on the card.

Target Market(s)

Southeast Asia, US, EU

Industry/Entity Type

Medical Equipment

Contact Information for Business Card

Below are the content we want to be shown on the business card(please help us to simplified them to be more presentable and readable):

Company name: Orlane (Hong Kong) 5K Medical Technology Company Limited
Address: Unit 2204, 22/F, Pebble Tower, No.8 Kendrick Lane, Wan Kei Shan, Hong Kong.
Band Name: Q5K
Homepage: www.orlane5kbq.example
Name: Lok Wing Sze
Title: Manager
Tel: +852-xxxx-xxxx
Mobile: +852-xxxx-xxxx
Email: xx@orlane5kbq.example

Production Lines:
China: Pei Ling Sun Ke Medical Technology Company Limited
Mo Lan City Rui Fa Textile Machinery Company Limited
Bangladesh: Q5K Medical Technology Company Limited

Qualifications:
ISO 13485:2016
ISO 14644-1:2015
ISO Class 8 Cleanroom
ASTM F2100 Level 2
EN14683 Type IIR
EN149 FFP2
CE Certified
FDA Registration number: XXX

Requirements
Must have
• use pantone color for the design
and provide the pantone number for printing purpose
Should not have
• Background color should not be black.

```html
<!DOCTYPE html>
<html lang="en">
<head>
<meta charset="utf-8">
<title>Q5K Business Card</title>
<link href="https://fonts.googleapis.com/css2?family=Roboto:wght@300;400;700&display=swap" rel="stylesheet">
<style>
  :root {
    --pink: #e8185a;
    --teal: #2ab3b1;
    --paper: #ffffff;
    --backdrop: #e6e8ea;
  }
  * { box-sizing: border-box; margin: 0; padding: 0; }
  html, body {
    width: 1200px; height: 901px; overflow: hidden;
    background: var(--backdrop);
    font-family: "Roboto", Arial, sans-serif;
  }
  .stage {
    width: 1200px; height: 901px;
    display: flex; flex-direction: column; align-items: center; justify-content: center;
    gap: 36px;
  }
  .card {
    position: relative;
    width: 660px; height: 377px;
    background: var(--paper);
    box-shadow: 0 6px 18px rgba(0,0,0,.15);
    overflow: hidden;
  }
  .card::after {
    content: ""; position: absolute; left: 0; right: 0; bottom: 0;
    height: 9px; background: var(--pink);
  }

  /* back side */
  .card-back { text-align: center; padding-top: 48px; }
  .brand {
    display: inline-flex; align-items: center; gap: 12px;
    color: var(--pink); font-weight: 700; font-size: 54px; letter-spacing: 2px; line-height: 1;
  }
  .brand-dot { width: 18px; height: 18px; border-radius: 50%; background: var(--teal); }
  .lines { margin-top: 22px; color: var(--teal); font-size: 17px; font-weight: 400; line-height: 1.4; }
  .label { color: var(--pink); }
  .quals-title { margin-top: 8px; color: var(--pink); font-weight: 700; font-size: 16px; letter-spacing: .5px; }
  .quals { color: var(--teal); font-size: 17px; line-height: 1.45; }

  /* front side */
  .card-front { display: flex; padding: 0 40px; }
  .company {
    width: 290px; display: flex; align-items: center; gap: 12px;
    padding-top: 10px; margin-bottom: 70px;
  }
  .company-dot { width: 16px; height: 16px; border-radius: 50%; background: var(--teal); flex: none; }
  .company-name { color: var(--pink); font-weight: 700; font-size: 40px; letter-spacing: 1px; }
  .divider { width: 1.5px; background: var(--teal); margin: 80px 26px 120px 0; }
  .person { padding-top: 92px; }
  .person-name { color: var(--pink); font-weight: 700; font-size: 30px; }
  .person-title { color: var(--teal); font-size: 19px; font-weight: 400; margin-top: 2px; }
  .contacts { list-style: none; margin-top: 22px; }
  .contacts li {
    display: flex; align-items: center; gap: 14px;
    color: var(--teal); font-size: 20px; line-height: 1.5;
  }
  .contacts svg { width: 18px; height: 18px; flex: none; fill: none; stroke: var(--pink); stroke-width: 2; }
  .address {
    position: absolute; left: 0; right: 0; bottom: 34px;
    text-align: center; color: var(--teal); font-size: 18.5px;
  }
</style>
</head>
<body>
<main class="stage">
  <section class="card card-back">
    <div class="brand"><span class="brand-dot"></span>Q5K</div>
    <div class="lines">
      <p><span class="label">China:</span> Pei Ling Sun Ke Medical Technology Company Limited</p>
      <p>Mo Lan City Rui Fa Textile Machinery Company Limited</p>
      <p><span class="label">Bangladesh:</span> Q5K Medical Technology Company Limited</p>
    </div>
    <p class="quals-title">QUALIFICATIONS:</p>
    <div class="quals">
      <p>ISO 13485:2016 &nbsp;|&nbsp; ISO 14644-1:2015</p>
      <p>ISO Class 8 Cleanroom &nbsp;|&nbsp; ASTM F2100 Level 2 &nbsp;|&nbsp; EN14683 Type IIR</p>
      <p>EN149 FFP2 &nbsp;|&nbsp; CE Certified &nbsp;|&nbsp; FDA Registration number: XXX</p>
    </div>
  </section>

  <section class="card card-front">
    <div class="company"><span class="company-dot"></span><span class="company-name">TAVMOREN</span></div>
    <div class="divider"></div>
    <div class="person">
      <p class="person-name">Lok Wing Sze</p>
      <p class="person-title">Manager</p>
      <ul class="contacts">
        <li><svg viewBox="0 0 24 24"><path d="M5 3h4l2 5-3 2a12 12 0 0 0 6 6l2-3 5 2v4a2 2 0 0 1-2 2A17 17 0 0 1 3 5a2 2 0 0 1 2-2z"/></svg>+852-xxxx-xxxx</li>
        <li><svg viewBox="0 0 24 24"><rect x="6" y="2" width="12" height="20" rx="2"/><path d="M11 18h2"/></svg>+852-xxxx-xxxx</li>
        <li><svg viewBox="0 0 24 24"><rect x="3" y="5" width="18" height="14" rx="1"/><path d="M3 6l9 7 9-7"/></svg>xx@orlane5kbq.example</li>
        <li><svg viewBox="0 0 24 24"><circle cx="12" cy="12" r="9"/><path d="M3 12h18M12 3c3 3 3 15 0 18M12 3c-3 3-3 15 0 18"/></svg>www.orlane5kbq.example</li>
      </ul>
    </div>
    <p class="address">Unit 2204, 22/F, Pebble Tower, No.8 Kendrick Lane, Wan Kei Shan, Hong Kong</p>
  </section>
</main>
</body>
</html>
```